Mobile Tutoring Service needs a Flier for Distribution to Clients

Lantern Scholars Inc. is a tutoring company that uses video call technology to perform tutoring session in math, sciences, and standardized test preparation. We need a flier that we can distribute to email lists of parents in school districts around the St. Louis Area, as well as post in public areas to attract clients. The following file has the important information needed on the flier. In particular, the "How it Works" Steps 1-3 can be made into an animation or video that looks attractive and helps potential clients understand our process. Our logo is also found in the document. Ideally, all information in the power point slide will be in the flier.

Target Market(s)

Parents for middle and high schoolers grade 6-12 in the St. Louis Area

Industry/Entity Type

Tutoring

Font styles to use
Serif

Colors
3176b5
85abd2
0492cd
33a6d7
ceeaf5

Requirements
Must have
• All the information with the attached file
Nice to have
• A nice-looking animation instead of the still screen shoots that are included in the attached file.

```html
<!DOCTYPE html>
<html lang="en">
<head>
<meta charset="utf-8">
<title>Lantern Scholars – Tutoring Flier</title>
<link rel="stylesheet" href="https://fonts.googleapis.com/css2?family=Montserrat:wght@700;800&family=Roboto+Condensed:ital,wght@0,400;0,700;1,700&display=swap">
<style>
  :root {
    --brand-blue: #4a8bd0;
    --brand-blue-deep: #3176b5;
    --ink: #231f20;
    --text: #222426;
    --paper: #ffffff;
    --stage: #e9e7e4;
    --step-top: #6b7380;
  }
  * { margin: 0; padding: 0; box-sizing: border-box; }
  html, body { width: 1200px; height: 1200px; overflow: hidden; background: var(--stage); }
  body { position: relative; font-family: "Roboto Condensed", sans-serif; color: var(--text); }

  .flier {
    position: absolute; left: 165px; top: 38px;
    width: 1011px; height: 1306px;
    transform: scale(0.86); transform-origin: top left;
    background: var(--paper); overflow: hidden;
    box-shadow: 0 10px 30px rgba(0,0,0,0.25);
  }
  .flier > * { position: absolute; }
  .shapes { left: 0; top: 0; width: 1011px; height: 1306px; }

  .brand-name {
    left: 677px; top: 282px; transform: translateX(-50%);
    font-family: "Montserrat", sans-serif; font-weight: 800; font-size: 48px;
    color: var(--ink); white-space: nowrap; letter-spacing: -0.5px;
  }
  .tagline { left: 677px; transform: translateX(-50%); white-space: nowrap; text-align: center; }
  .tagline--main { top: 342px; font-size: 58px; color: var(--brand-blue); }
  .tagline--sub { top: 408px; font-size: 39px; color: var(--brand-blue); }
  .tagline--sub em { font-weight: 700; }
  .tagline--device { top: 460px; font-size: 38px; font-weight: 700; color: var(--ink); }

  .info { left: 538px; width: 395px; font-size: 24px; line-height: 30px; }
  .info h3 { font-size: 24px; font-weight: 700; }
  .info--subjects { top: 572px; }
  .info--tutors { top: 692px; }
  .info--schedule { top: 812px; }

  .payment-title { left: 538px; top: 942px; font-size: 40px; font-weight: 700; color: var(--ink); }
  .payment-plans { left: 535px; top: 1014px; width: 420px; color: var(--paper); }
  .payment-plans p { font-size: 24px; line-height: 30px; }
  .payment-plans strong { display: block; font-style: italic; font-weight: 700; font-size: 31px; line-height: 38px; margin-top: 4px; }

  .step { display: flex; flex-direction: column; align-items: center; justify-content: center; text-align: center; color: var(--paper); transform: translate(-50%, -50%); white-space: nowrap; }
  .step b { font-weight: 400; font-size: 42px; line-height: 44px; }
  .step span { font-size: 24px; line-height: 30px; }
  .step--one { left: 147px; top: 709px; }
  .step--two { left: 147px; top: 893px; }
  .step--three { left: 150px; top: 1075px; }

  .cta { left: 505px; transform: translateX(-50%); white-space: nowrap; }
  .cta--headline { top: 1204px; font-size: 28px; font-weight: 700; color: var(--paper); }
  .cta--contacts { top: 1240px; font-size: 30px; color: var(--brand-blue); word-spacing: 2px; }
  .cta--contacts .divider { color: var(--brand-blue); margin: 0 18px; }
</style>
</head>
<body>
<main class="flier">
  <svg class="shapes" viewBox="0 0 1011 1306" xmlns="http://www.w3.org/2000/svg">
    <defs>
      <linearGradient id="photo-tones" x1="0" y1="0" x2="1" y2="0">
        <stop offset="0" stop-color="#d8cdc2"/>
        <stop offset="0.3" stop-color="#c9a89a"/>
        <stop offset="0.55" stop-color="#e3ddd8"/>
        <stop offset="1" stop-color="#f3f5f8"/>
      </linearGradient>
      <linearGradient id="step-fill" x1="0" y1="0" x2="0" y2="1">
        <stop offset="0" stop-color="var(--step-top)"/>
        <stop offset="0.55" stop-color="#4a8bd0"/>
      </linearGradient>
    </defs>

    <rect class="hero-photo" x="0" y="150" width="1011" height="1000" fill="url(#photo-tones)" role="img" aria-label="Photo of a smiling teenage student with a backpack using a smartphone on a blurred city street"/>

    <polygon class="header-band" points="0,0 1011,0 1011,50 555,124 0,196" fill="var(--brand-blue)"/>
    <polygon class="header-stripe" points="0,196 555,118 555,128 0,226" fill="var(--ink)"/>
    <circle class="header-disc" cx="669" cy="130" r="116" fill="var(--paper)"/>

    <polygon class="info-panel" points="509,516 748,556 968,516 968,1160 509,1160" fill="rgba(255,255,255,0.85)"/>
    <polygon class="info-fold" points="509,562 509,680 285,805" fill="var(--paper)"/>
    <line x1="509" y1="562" x2="285" y2="805" stroke="var(--brand-blue)" stroke-width="5"/>
    <polyline points="509,516 748,556 968,516" fill="none" stroke="var(--brand-blue)" stroke-width="7"/>

    <rect class="footer-band" x="0" y="1134" width="1011" height="172" fill="var(--ink)"/>
    <polygon class="payment-box" points="509,996 968,996 968,1160 735,1192 509,1160" fill="var(--brand-blue)"/>

    <circle class="step-disc" cx="147" cy="709" r="90" fill="url(#step-fill)" stroke="var(--paper)" stroke-width="2"/>
    <circle class="step-disc" cx="147" cy="893" r="110" fill="url(#step-fill)" stroke="var(--paper)" stroke-width="2"/>
    <circle class="step-disc" cx="150" cy="1075" r="112" fill="url(#step-fill)" stroke="var(--paper)" stroke-width="2"/>
  </svg>

  <h1 class="brand-name">Lantern Scholars</h1>
  <p class="tagline tagline--main">Personalized tutoring</p>
  <p class="tagline tagline--sub">in <em>MATH</em> and <em>SCIENCE</em> via your</p>
  <p class="tagline tagline--device">MOBILE DEVICE</p>

  <section class="info info--subjects">
    <h3>Subjects:</h3>
    <p>All Math, Science, Standardized Test Prep, and Writing 6th-12th grade.</p>
  </section>
  <section class="info info--tutors">
    <h3>Our tutors are local</h3>
    <p>St. Louis PhD candidates or PhD degree holders in STEM fields.</p>
  </section>
  <section class="info info--schedule">
    <h3>No scheduling required!</h3>
    <p>As soon as you send a message for help, a tutor will respond to set up a study session as soon as possible.</p>
  </section>

  <h2 class="payment-title">Payment Plans:</h2>
  <div class="payment-plans">
    <p>Pay-as-you-go: $0.83/minute. $0 up-front before session begins!</p>
    <strong>Unlimited Subscription:<br>$150 per month</strong>
  </div>

  <div class="step step--one"><b>STEP 1</b><span>Send Tutors<br>Your Problem</span></div>
  <div class="step step--two"><b>STEP 2</b><span>Tutor Sends<br>Response to set<br>up session</span></div>
  <div class="step step--three"><b>STEP 3</b><span>Perform Tutoring<br>Session and Receive<br>Copy of your notes!</span></div>

  <p class="cta cta--headline">CONTACT US TODAY TO SET UP FOR YOUR FIRST, FREE TUTORING SESSION</p>
  <p class="cta cta--contacts">www.lanternscholars.com<span class="divider">|</span>866-555-0142<span class="divider">|</span>tutor@lanternscholars.com</p>
</main>
</body>
</html>
```